House-share and Room Rental Website (With Focus on the Bedroom Landing Page)

Looking for website design for our House-share (executive accommodation) and room rental business.

Our company name is: Lodvenra could also be written as LodVenra or lodvenra. Either is fine .. just looking for a nice clean catchy logo to go with the design.

EXAMPLES
These are examples of other websites in this field that are doing well. this is a kind of baseline.
https://kelbrin.com.au/
https://www.tuvaplex.com/
https://www.nestorvi.com/
https://www.quillsa.net/
https://www.pendlebarrow.com.au/

Our business model is to rent rooms to people looking for high-quality accommodation. We fill the gap between those looking to rent rooms and those with rooms to rent. However, our model is slightly different from those already on the market as we looking to fill a massive gap in the market delivering upmarket rooms for rent.(Executive Accommodation) also in the back end will be coupled with a self management process in the back end.

We offer executive style accommodation that stands out above the rest. With special extras like fire safety.. and management processes that create happier homes. We are looking for a web design package that can help us grow and scale our business. We need a design that is captivating

Our MAIN focus is having a room landing page that stands out from the rest... The core of our business will rely on the promotion of the rooms in a share house... so the whole design relies on the BEDROOM landing page to drive results.

Target Market(s)

We have 2 markets we are aiming at ... the first market is people offering rooms to rent who want the highest rental return. The second market is people looking to rent safe, high-quality rooms, in houses that are well managed and looked after.

Industry/Entity Type

Share Economy

Logo Text

LodVenra

Number of Pages Required

5+ page

Font styles to use
Sans Serif

Colors
3276b5

Requirements
Must have
• A messaging system whereby we can create direct communication between those offering rooms and those looking for rooms.
• A call to action that says " Schedule an Inspection"
• Landing page for promoting rooms
• A home page for showing stock.
• Profile page for those selling rooms
• Profile page for those looking for rooms.
• A scheduling calendar for booking inspections
Nice to have
• Pages where new residents can lock in a room.. pay bond and rents.. and sign contracts
• Notifications
• SMS capabilities in the backend.
Should not have
• No script or handwriting fonts.

```html
<!DOCTYPE html>
<html lang="en">
<head>
<meta charset="UTF-8">
<title>Room amenities</title>
<link href="https://fonts.googleapis.com/css2?family=Dosis:wght@300;400;500;600;700&display=swap" rel="stylesheet">
<style>
  :root {
    --brand-blue: #3276b5;
    --text-dark: #2b2b2b;
    --text-body: #333333;
    --text-muted: #9a9a9a;
    --section-grey: #efefef;
    --page-white: #ffffff;
    --bullet-blue: #3276b5;
  }
  * { box-sizing: border-box; margin: 0; padding: 0; }
  html, body {
    width: 1200px;
    height: 1000px;
    overflow: hidden;
    background: var(--page-white);
    font-family: "Dosis", sans-serif;
    color: var(--text-body);
  }
  .page { position: relative; width: 1200px; height: 1000px; }

  .intro {
    position: absolute;
    top: 0; left: 0;
    width: 1200px; height: 368px;
    background: var(--page-white);
  }
  .intro__copy {
    position: absolute;
    left: 112px; top: 27px;
    width: 618px;
    font-size: 14.2px;
    line-height: 22.6px;
    font-weight: 400;
    color: var(--text-body);
  }
  .intro__copy strong { font-weight: 700; color: var(--text-dark); }
  .intro__note {
    position: absolute;
    left: 112px; top: 162px;
    width: 618px;
    font-size: 14.2px;
    line-height: 22.6px;
    font-weight: 400;
    color: var(--text-muted);
  }
  .cta-button {
    position: absolute;
    left: 112px; top: 246px;
    width: 217px; height: 47px;
    border: 1px solid var(--brand-blue);
    color: var(--brand-blue);
    background: transparent;
    font-family: "Dosis", sans-serif;
    font-size: 16px;
    font-weight: 500;
    letter-spacing: 0.2px;
    text-transform: uppercase;
    display: flex; align-items: center; justify-content: center;
    text-decoration: none;
  }

  .amenities {
    position: absolute;
    top: 368px; left: 0;
    width: 1200px; height: 600px;
    background: var(--section-grey);
  }
  .amenities__title {
    position: absolute;
    left: 108px; top: 103px;
    font-size: 46px;
    font-weight: 300;
    line-height: 56px;
    color: var(--text-dark);
    letter-spacing: -0.3px;
  }
  .amenities__subtitle {
    position: absolute;
    left: 111px; top: 159px;
    font-size: 16.5px;
    font-weight: 300;
    color: var(--text-muted);
  }
  .amenities__list {
    position: absolute;
    left: 110px; top: 215px;
    list-style: none;
  }
  .amenities__item {
    position: relative;
    height: 33px;
    padding-left: 23px;
    font-size: 16.5px;
    font-weight: 300;
    line-height: 24px;
    color: var(--text-dark);
  }
  .amenities__item::before {
    content: "";
    position: absolute;
    left: 1px; top: 8px;
    width: 5px; height: 5px;
    border: 1px solid var(--bullet-blue);
    border-radius: 50%;
  }
  .amenities__photo {
    position: absolute;
    left: 603px; top: 116px;
    width: 486px; height: 373px;
    background:
      radial-gradient(ellipse at 78% 60%, rgba(120,160,70,0.55) 0%, rgba(120,160,70,0.15) 28%, rgba(255,255,255,0) 45%),
      linear-gradient(135deg, #f7f6f3 0%, #eeebe4 45%, #e3ddd1 100%);
    box-shadow: 0 8px 22px rgba(0,0,0,0.12);
  }
</style>
</head>
<body>
<main class="page">
  <section class="intro">
    <p class="intro__copy"><strong>Aenean convallis sit amet</strong> enim lacinia maximus. Lorem ipsum dolor sit amet, consectetur adipiscing elit. Cras dignissim, lorem sit amet consequat tempor, erat mi dapibus nibh, quis vehicula nisi lectus ac leo. Maecenas ultricies a ex ut tincidunt. Nullam justo ipsum, lobortis quis mauris et, dignissim ullamcorper nisl. Nunc nec felis a turpis congue molestie ac id orci. Donec venenatis est eget ultrices gravida. Praesent porttitor commodo hendrerit. Mauris laoreet urna in quam lacinia tincidunt.</p>
    <p class="intro__note">Pellentesque habitant morbi tristique senectus et netus et malesuada fames ac turpis egestas. Duis ultrices egestas erat eget rhoncus.</p>
    <a class="cta-button" href="#">Schedule an inspection</a>
  </section>

  <section class="amenities">
    <h2 class="amenities__title">Room amenities</h2>
    <p class="amenities__subtitle">Lorem ipsum dolor sit amet</p>
    <ul class="amenities__list">
      <li class="amenities__item">Fully furnished</li>
      <li class="amenities__item">TV</li>
      <li class="amenities__item">Storage space</li>
      <li class="amenities__item">Study Desk</li>
      <li class="amenities__item">Wardrobe</li>
      <li class="amenities__item">Ensuite shower</li>
      <li class="amenities__item">Kitchenette</li>
    </ul>
    <div class="amenities__photo" role="img" aria-label="Bright white bedroom interior with a bamboo plant in the foreground"></div>
  </section>
</main>
</body>
</html>
```